New Managed IT company needs a business card

We are an IT management and support company that needs a business card design. I have a logo that I'll provide. Blues and blacks match the logo, but i'm open to anything. I want the card to help people take us seriously, but still have some energy and fun in it. The card should communicate stability and a solid company.

Target Market(s)

Target market includes Owners and Presidents at small businesses of 20 - 100 employees in the Pittsburgh PA area.

Industry/Entity Type

Information Technology

Contact Information for Business Card

i am open to other designs, but i imagine having only the logo on one side and then the logo plus all contact details on the other side.

Requirements
Must have
• Our logo
• Company name is optional if the logo makes it obvious
• A name - Lew Tasker
• A title - President
• A phone number - 724-XXX-XXXX
• A mobile phone number - 724-516-0471
• An email address - ltasker@brightlanetech.com
• a website - brightlanetech.com or www.brightlanetech.com
Nice to have
• some people tell me the logo feels like a superhero theme, some fun with that idea might be good. I'm open to ideas.
Should not have
• stock photos of people or computers - especially old looking stuff.

```html
<!DOCTYPE html>
<html lang="en">
<head>
<meta charset="utf-8">
<title>Brightlane Tech – Business Card</title>
<link rel="stylesheet" href="https://fonts.googleapis.com/css2?family=Exo+2:wght@500;600;700&family=Open+Sans:wght@400;600&display=swap">
<style>
  :root {
    --backdrop: #e9e6e1;
    --card-white: #ffffff;
    --card-black: #0b0c0e;
    --accent-blue: #2aa3e6;
    --accent-blue-deep: #1f6fc4;
    --ink-grey: #2b2d31;
    --text-light: #e8eaee;
    --text-muted: #b9bec6;
  }
  * { box-sizing: border-box; margin: 0; padding: 0; }
  html, body {
    width: 1200px; height: 1023px; overflow: hidden;
    background: var(--backdrop);
  }
  .stage {
    width: 1200px; height: 1023px;
    display: flex; align-items: center; justify-content: center; gap: 60px;
  }
  .card {
    position: relative;
    width: 525px; height: 300px;
    overflow: hidden;
    background: var(--card-white);
    box-shadow: 0 10px 28px rgba(0,0,0,.18);
  }
  .card-front__shape { position: absolute; inset: 0; }
  .brand-mark {
    position: absolute; left: 26px; top: 50%; transform: translateY(-50%);
    display: flex; flex-direction: column; align-items: flex-start; gap: 12px;
  }
  .brand-mark__dot {
    width: 54px; height: 54px; border-radius: 50%;
    background: var(--accent-blue);
  }
  .brand-mark__name {
    font-family: "Exo 2", sans-serif; font-weight: 700;
    font-size: 22px; line-height: 1.05; letter-spacing: 2px;
    text-transform: uppercase; color: var(--accent-blue);
  }
  .contact {
    position: absolute; left: 268px; top: 58px;
    color: var(--text-light);
  }
  .contact__name {
    font-family: "Exo 2", sans-serif; font-weight: 600;
    font-size: 25px; letter-spacing: 1px; font-variant: small-caps;
    color: var(--accent-blue);
  }
  .contact__title {
    font-family: "Open Sans", sans-serif; font-size: 14px;
    color: var(--text-muted); margin-top: 2px;
  }
  .contact__list { list-style: none; margin-top: 26px; }
  .contact__item {
    display: flex; align-items: center; gap: 10px;
    font-family: "Open Sans", sans-serif; font-size: 14.5px;
    line-height: 24px; color: var(--text-light);
  }
  .contact__icon { width: 14px; height: 14px; fill: var(--accent-blue); flex: none; }
  .card-back {
    display: flex; align-items: center; justify-content: center; gap: 18px;
  }
  .card-back .brand-mark__dot { width: 64px; height: 64px; background: var(--ink-grey); }
  .card-back__name {
    font-family: "Exo 2", sans-serif; font-weight: 700;
    font-size: 36px; letter-spacing: 4px; text-transform: uppercase;
    color: var(--ink-grey);
  }
</style>
</head>
<body>
<main class="stage">
  <section class="card card-front" aria-label="Card front with contact details">
    <svg class="card-front__shape" viewBox="0 0 525 300" aria-hidden="true">
      <polygon points="0,0 70,0 0,70" fill="var(--card-black)"/>
      <polygon points="0,230 70,300 0,300" fill="var(--card-black)"/>
      <polygon points="240,0 525,0 525,300 240,300 190,150" fill="var(--card-black)"/>
    </svg>
    <div class="brand-mark">
      <span class="brand-mark__dot"></span>
      <span class="brand-mark__name">Brightlane<br>Tech</span>
    </div>
    <div class="contact">
      <h1 class="contact__name">Lew Tasker</h1>
      <p class="contact__title">President</p>
      <ul class="contact__list">
        <li class="contact__item">
          <svg class="contact__icon" viewBox="0 0 16 16" aria-hidden="true"><path d="M3.5 1l2.5 3-1.5 2c1 2 2.5 3.5 4.5 4.5l2-1.5 3 2.5-1.5 2.5C6.5 14 2 9.5 1 2.5z"/></svg>
          <span>724-XXX-XXXX</span>
        </li>
        <li class="contact__item">
          <svg class="contact__icon" viewBox="0 0 16 16" aria-hidden="true"><path d="M4 1h8v14H4zM5.5 3v9h5V3z"/></svg>
          <span>724-516-0471</span>
        </li>
        <li class="contact__item">
          <svg class="contact__icon" viewBox="0 0 16 16" aria-hidden="true"><path d="M1 3h14v10H1zM2.5 4.5L8 9l5.5-4.5z"/></svg>
          <span>ltasker@brightlanetech.com</span>
        </li>
        <li class="contact__item">
          <svg class="contact__icon" viewBox="0 0 16 16" aria-hidden="true"><circle cx="8" cy="8" r="7"/><path d="M1 8h14M8 1c-3 3-3 11 0 14M8 1c3 3 3 11 0 14" stroke="var(--card-black)" stroke-width="1" fill="none"/></svg>
          <span>www.brightlanetech.com</span>
        </li>
      </ul>
    </div>
  </section>

  <section class="card card-back" aria-label="Card back with company name">
    <span class="brand-mark__dot"></span>
    <span class="card-back__name">Brightlane Tech</span>
  </section>
</main>
</body>
</html>
```